IT services provider needs a go to market lifecycle design

We need our go to market lifecycle diagram to be developed to show the flow of our propositions. We believe that customers could engage us at any stage of the cycle and that it would lead on to the next proposition, or, they could join at the start (Assess and Advice) and we would provide them with our services throughout the cycle.

```html
<!DOCTYPE html>
<html lang="en">
<head>
<meta charset="utf-8">
<title>Data Centre Workspace Lifecycle</title>
<link rel="stylesheet" href="https://fonts.googleapis.com/css2?family=Open+Sans:wght@700&family=Carlito:wght@700&display=swap">
<style>
  :root {
    --teal: #3a92a6;
    --purple: #4a2c82;
    --white: #ffffff;
    --bg: #ffffff;
  }
  html, body {
    margin: 0;
    padding: 0;
    width: 1125px;
    height: 1200px;
    overflow: hidden;
    background: var(--bg);
  }
  .lifecycle {
    position: relative;
    width: 1125px;
    height: 1200px;
  }
  .lifecycle-ring {
    position: absolute;
    inset: 0;
  }
  .stage { stroke: var(--white); stroke-width: 10; stroke-linejoin: miter; }
  .stage--teal { fill: var(--teal); }
  .stage--purple { fill: var(--purple); }
  .stage-label {
    font-family: "Open Sans", Arial, sans-serif;
    font-weight: 700;
    font-size: 36px;
    letter-spacing: 0.5px;
    fill: var(--white);
  }
  .hub-title {
    position: absolute;
    left: 0;
    right: 0;
    top: 468px;
    margin: 0;
    text-align: center;
    font-family: "Carlito", "Calibri", Arial, sans-serif;
    font-weight: 700;
    font-size: 92px;
    line-height: 94px;
    color: var(--purple);
  }
</style>
</head>
<body>
<main class="lifecycle">
  <svg class="lifecycle-ring" width="1125" height="1200" viewBox="0 0 1125 1200" aria-label="Lifecycle: Assess &amp; Advise, Architect &amp; Transform, Manage &amp; Operate, Recycle &amp; Retire">
    <defs>
      <path id="arc-recycle" d="M134.4 548.1 A430 430 0 0 1 673.3 177.7"/>
      <path id="arc-assess" d="M606.9 165.4 A430 430 0 0 1 977.3 704.3"/>
      <path id="arc-architect" d="M444.5 1031.5 A454 454 0 0 0 1013.5 640.5"/>
      <path id="arc-manage" d="M123.5 475.5 A454 454 0 0 0 514.5 1044.5"/>
    </defs>

    <path class="stage stage--teal" d="M32.9 537.4 A532 532 0 0 1 617.6 63.9 L676.4 166.1 L598.8 242.9 A352 352 0 0 0 211.9 556.2 L135.1 478.6 Z"/>
    <path class="stage stage--purple" d="M617.6 63.9 A532 532 0 0 1 1091.1 648.6 L989.0 707.4 L912.1 629.8 A352 352 0 0 0 598.8 242.9 L676.4 166.1 Z"/>
    <path class="stage stage--teal" d="M1091.1 648.6 A532 532 0 0 1 506.4 1122.1 L447.6 1019.9 L525.2 943.1 A352 352 0 0 0 912.1 629.8 L989.0 707.4 Z"/>
    <path class="stage stage--purple" d="M506.4 1122.1 A532 532 0 0 1 32.9 537.4 L135.1 478.6 L211.9 556.2 A352 352 0 0 0 525.2 943.1 L447.6 1019.9 Z"/>

    <text class="stage-label"><textPath href="#arc-recycle" startOffset="50%" text-anchor="middle">RECYCLE &amp; RETIRE</textPath></text>
    <text class="stage-label"><textPath href="#arc-assess" startOffset="50%" text-anchor="middle">ASSESS &amp; ADVISE</textPath></text>
    <text class="stage-label"><textPath href="#arc-architect" startOffset="50%" text-anchor="middle">ARCHITECT &amp; TRANSFORM</textPath></text>
    <text class="stage-label"><textPath href="#arc-manage" startOffset="50%" text-anchor="middle">MANAGE &amp; OPERATE</textPath></text>
  </svg>

  <h1 class="hub-title">Data Centre<br>Workspace</h1>
</main>
</body>
</html>
```